Book cover for "Eczema turnaround"

Hi, we need a book cover for "Eczema turnaround" book.
It's a book about how to cure psoriasis symptoms which appeared to be results of stress.
The main theme in this book is that all symptoms are psychosomatic and can be cut short by reducing the level of stress.
Cover has to be bold and speaking. It has to show the results,
PLEASE consider using photos or illustrations "before" and "after".
Or maybe you can propose your vision.

3D image and 2D image.
Please see the links, it will be helpful for you to create image form.
http://kx7wqrna.lumvexo.com/?skip-tracking=true
http://tz3mbfuc.lumvexo.com/?skip-tracking=true

Target Market(s)

TA is very wide, it's all people who experienced decease demonstration. Usually these people very embarrassed of their illness, they are under high level of stress and what they need it's hope and believe that they can relief their condition.

Requirements
Must have
• Author name:
Pavel Drenko
Titlle :
Eczema turnaround
Subtitle:
ECZEMA TURNAROUND:
REDUCE THE RASH AND ITCHING 73% WITH THIS SIMPLE TECHNIQUE

```html
<!DOCTYPE html>
<html lang="en">
<head>
<meta charset="utf-8">
<title>Eczema Turnaround — Book Cover</title>
<link rel="stylesheet" href="https://fonts.googleapis.com/css2?family=Barlow:wght@400;700&family=Marcellus&display=swap">
<style>
  :root {
    --paper: #ffffff;
    --teal: #1ba3a8;
    --title-teal: #17999b;
    --plum: #6e2d5c;
    --pink-soft: #f7c2ea;
    --pink: #f07bd6;
    --lilac: #c9b2f2;
    --ring-grey: #d6d6d6;
  }
  * { margin: 0; padding: 0; box-sizing: border-box; }
  html, body {
    width: 849px;
    height: 1200px;
    overflow: hidden;
    background: var(--paper);
  }
  .cover {
    position: relative;
    width: 849px;
    height: 1200px;
    background: var(--paper);
    overflow: hidden;
  }
  .subtitle {
    position: absolute;
    top: 74px;
    left: 0;
    width: 100%;
    text-align: center;
    font-family: "Barlow", sans-serif;
    font-weight: 400;
    font-size: 39px;
    line-height: 51px;
    letter-spacing: 0.02em;
    color: var(--teal);
    text-transform: uppercase;
  }
  .subtitle strong { font-weight: 700; }
  .art-area {
    position: absolute;
    left: 20px;
    top: 287px;
    width: 807px;
    height: 706px;
    background: linear-gradient(135deg, var(--pink-soft) 0%, var(--lilac) 50%, var(--pink) 100%);
  }
  .title-disc {
    position: absolute;
    left: 214px;
    top: 398px;
    width: 426px;
    height: 426px;
  }
  .title-disc svg { position: absolute; inset: 0; overflow: visible; }
  .title {
    position: absolute;
    left: 0;
    top: 0;
    width: 426px;
    height: 426px;
    display: flex;
    flex-direction: column;
    align-items: center;
    justify-content: center;
    font-family: "Marcellus", serif;
    font-weight: 400;
    color: var(--title-teal);
    text-align: center;
    padding-bottom: 28px;
  }
  .title-main {
    font-size: 78px;
    line-height: 1;
    letter-spacing: 0.01em;
  }
  .title-sub {
    font-size: 38px;
    line-height: 1;
    margin-top: 8px;
    letter-spacing: 0.05em;
  }
  .author {
    position: absolute;
    top: 1062px;
    left: 0;
    width: 100%;
    text-align: center;
    font-family: "Barlow", sans-serif;
    font-weight: 700;
    font-size: 39px;
    letter-spacing: 0.1em;
    color: var(--plum);
    text-transform: uppercase;
  }
</style>
</head>
<body>
  <main class="cover">
    <p class="subtitle">Reduce the rash and itching<br><strong>73%</strong> with this simple technique</p>

    <div class="art-area" role="img" aria-label="Decorative watercolour splash in pink, magenta, lilac, blue and cyan behind the title circle"></div>

    <div class="title-disc">
      <svg width="426" height="426" viewBox="0 0 426 426" aria-hidden="true">
        <circle cx="220" cy="222" r="222" fill="var(--ring-grey)" opacity="0.7"/>
        <circle cx="213" cy="213" r="213" fill="var(--paper)"/>
      </svg>
      <h1 class="title">
        <span class="title-main">ECZEMA</span>
        <span class="title-sub">TURNAROUND</span>
      </h1>
    </div>

    <p class="author">Pavel Drenko</p>
  </main>
</body>
</html>
```